Banner Ad for a Holding Page of a Website - Power Parcel

We require a sort of banner ad or an impactful image to use in the holding page, while we work on a final worksite, while providing basic information about the project.
In other words, a nice image instead of (or in addition to) using the boring "under construction" text.
The project is a new service, which consists of sending highly trained energy efficiency technicians to homes for a 2 hour intervention in order to help householders improve the energy efficiency of their homes. These interventions consist of adjusting the central thermostat, maybe installing thermostatic valves on the radiators, low consumption lightbulbs, etc. In addition, these technicians will also provide the householders advise for improving the energy efficiency of their homes, e.g. length of showers, more efficient ways of cooking, washing, etc. I'm attaching a couple of ideas (banner 1 & 2) that I like in terms of nice and different images for the holding page banner. Also, feel free to google the following measures we install or adjust: thermostatic radiator valves, room or central thermostats, LED lightbulbs or low consumption light bulbs. Which might trigger some nice ideas for this banner. I'm looking forward to seeing your proposals or let me know if you need further information (I'm attaching also an initial write up about the project).

March 6th:
I've just added a file with the current thinking on the holding page (including a top logo). Please note the red section, which is the specific image briefed to Sketch Guild designers. The project is not the whole page, it is only the "under construction" image. Thanks

Target Market(s)

Mainly households interested in energy saving, due to high costs of energy, the environment or improving comfort.

Industry/Entity Type

Construction

Colors

Designer to choose colors to be used in the design.

Requirements
Must have
• Convey the idea of under construction or coming soon.
Creativity relevant to the project.

```html
<!DOCTYPE html>
<html lang="en">
<head>
<meta charset="utf-8">
<title>Power Parcel – We Will Be Back Soon</title>
<link rel="stylesheet" href="https://fonts.googleapis.com/css2?family=Lilita+One&display=swap">
<style>
  :root {
    --page-bg: #ffffff;
    --banner-top: #0b4f7c;
    --banner-mid: #0a3a5c;
    --banner-bottom: #081f33;
    --text-light: #ececec;
    --text-shadow: rgba(0, 0, 0, 0.45);
    --bulb-glass: #dfe6ea;
    --bulb-base: #8d949a;
  }
  * { margin: 0; padding: 0; box-sizing: border-box; }
  html, body {
    width: 1200px;
    height: 450px;
    overflow: hidden;
    background: var(--page-bg);
  }
  .canvas {
    position: relative;
    width: 1200px;
    height: 450px;
  }
  .holding-banner {
    position: absolute;
    left: 173px;
    top: 120px;
    width: 854px;
    height: 211px;
    background: linear-gradient(180deg, var(--banner-top) 0%, var(--banner-mid) 55%, var(--banner-bottom) 100%);
  }
  .bulb-visual {
    position: absolute;
    left: 50px;
    top: 15px;
    width: 108px;
    height: 188px;
    border-radius: 46px 46px 24px 24px;
    background: linear-gradient(180deg, var(--bulb-glass) 0%, var(--bulb-glass) 62%, var(--bulb-base) 100%);
    opacity: 0.9;
  }
  .banner-message {
    position: absolute;
    left: 200px;
    right: 52px;
    top: 50px;
    text-align: center;
    font-family: "Lilita One", "Arial Black", sans-serif;
    color: var(--text-light);
    text-transform: uppercase;
    text-shadow: 1px 2px 2px var(--text-shadow);
  }
  .banner-headline {
    font-size: 45px;
    line-height: 1;
    letter-spacing: 2px;
    font-weight: 400;
  }
  .banner-subline {
    margin-top: 16px;
    font-size: 26px;
    line-height: 1;
    letter-spacing: 1.4px;
    font-weight: 400;
  }
</style>
</head>
<body>
  <main class="canvas">
    <section class="holding-banner">
      <div class="bulb-visual" role="img" aria-label="Photo of a spiral low-consumption light bulb"></div>
      <div class="banner-message">
        <h1 class="banner-headline">We will be back soon</h1>
        <p class="banner-subline">Technicians are producing energy</p>
      </div>
    </section>
  </main>
</body>
</html>
```